Cloud backup company needs a new website

We need a new design for our website as the current one is quite dated now. You can view the current website at www.vaultmere-store.net.au to view the content elements.

We provide cloud backup services (ie remote off site to a cluster of servers) to small to medium businesses looking for better alternatives to tape or optical media backups.

Target Market(s)

SME/SMB (Businesses with fewer than 100 employees)

Industry/Entity Type

It Company

Requirements
Must have
• Must have sections to sign up to newsletter, log in to account, view news feed as per current website.

Must have a prominent call to action to sign up for a trial and view pricing.

Also like it to have twitter and facebook links/likes integration
Should not have
• No Flash, no serif fonts

```html
<!DOCTYPE html>
<html lang="en">
<head>
<meta charset="utf-8">
<title>vaultmere – Cloud Backup</title>
<link rel="stylesheet" href="https://fonts.googleapis.com/css2?family=PT+Sans:wght@400;700&family=Open+Sans:wght@400;600;700&family=Hind:wght@500;600;700&family=Lato:wght@400;700&display=swap">
<style>
:root{
  --orange:#f06a1c;
  --orange-deep:#e3581a;
  --orange-dark:#c9501a;
  --grey-bg:#f1f1f1;
  --ink:#333;
  --muted:#777;
  --dark:#2c2b2b;
  --dark-2:#3a3939;
  --white:#fff;
  --line:#e4e4e4;
  --social-a:#2f5d93;
  --social-b:#3fa9de;
}
*{box-sizing:border-box;margin:0;padding:0}
html,body{width:766px;height:1200px;overflow:hidden}
body{position:relative;background:var(--grey-bg);font-family:"Open Sans",sans-serif;color:var(--ink)}
svg{display:block}
.abs{position:absolute}
.orange-floor{left:0;top:866px;width:766px;height:334px;background:var(--orange)}

/* header */
.brand-box{left:77px;top:0;width:200px;height:83px;background:var(--white)}
.brand-name{left:80px;top:26px;font-family:"PT Sans",sans-serif;font-weight:400;font-size:27px;color:var(--orange);letter-spacing:.5px}
.utility{right:65px;top:9px;font-size:7.5px;color:#555;display:flex;gap:14px;align-items:center}
.utility .phone{display:flex;gap:6px;align-items:center}
.search{left:467px;top:41px;width:219px;height:21px;background:var(--white);border:1px solid #e6e6e6;font-size:10px;color:#bbb;padding:4px 14px}
.search-icon{left:695px;top:42px}

/* nav */
.main-nav{left:77px;top:83px;width:626px;height:30px;background:var(--orange)}
.main-nav a{position:absolute;top:0;height:30px;line-height:30px;color:var(--white);font-family:"Open Sans",sans-serif;font-weight:700;font-size:9.5px;text-decoration:none;text-align:center}
.main-nav .sep{position:absolute;top:0;width:1px;height:30px;background:#d95812;box-shadow:1px 0 0 #f5873f}
.social{top:4px;width:21px;height:22px;border-radius:3px;background:var(--social-a)}
.social.second{background:var(--social-b)}

/* content panel */
.panel{left:82px;top:113px;width:626px;height:860px;background:var(--white)}
.hero-photo{left:89px;top:133px;width:422px;height:199px;background:radial-gradient(ellipse at 45% 40%,#f7b03a 0%,#e46b12 40%,#7a2a08 85%,#3d1505 100%)}
.hero-side{left:511px;top:133px;width:178px;height:199px;background:linear-gradient(135deg,#3a2a1d,#1f1712)}
.hero-side h2{position:absolute;left:15px;top:22px;font-family:"PT Sans",sans-serif;font-weight:400;font-size:15.5px;line-height:20px;color:var(--white)}
.hero-side p{position:absolute;left:15px;top:73px;width:145px;font-size:6.8px;line-height:10.5px;color:#ddd}
.hero-side .more{position:absolute;left:15px;top:134px;font-size:6.8px;color:#fff;text-decoration:underline}
.hero-dots{left:268px;top:291px;display:flex;gap:8px}
.hero-dots i{width:5px;height:5px;border-radius:50%;background:#eee;display:block}
.hero-caption{left:89px;top:306px;width:600px;height:26px;background:rgba(30,30,30,.75);display:flex;align-items:center;gap:8px;padding-left:11px}
.hero-caption strong{font-family:"PT Sans",sans-serif;font-weight:400;font-size:11.5px;color:#fff}
.hero-caption span{font-size:7px;color:#ddd}

.cta-band{left:76px;top:332px;width:627px;height:43px;background:var(--orange);font-family:"Hind",sans-serif;font-weight:600;font-size:38px;line-height:46px;color:var(--white);padding-left:40px;white-space:nowrap}
.cta-band .num{font-size:34px;letter-spacing:1.5px;margin-left:10px;font-weight:700}

/* newsletter widget */
.news-widget{left:85px;top:381px;width:425px;height:71px;background:var(--dark);border-radius:4px}
.trial-tab{left:85px;top:381px;width:68px;height:71px;background:#f7a21e;border-radius:4px 0 0 4px}
.trial-tab .inner{position:absolute;left:6px;top:8px;width:62px;height:55px;background:var(--orange)}
.trial-tab span{position:absolute;left:36px;top:36px;transform:translate(-50%,-50%) rotate(-90deg);font-family:"PT Sans",sans-serif;font-size:15px;line-height:14px;color:#fff;text-align:center;white-space:nowrap}
.email-field{left:162px;top:389px;width:265px;height:17px;background:#fff;border:1px solid #ccc}
.mail-icon{left:435px;top:390px}
.widget-tabs{top:421px;font-family:"PT Sans",sans-serif;font-size:20px;color:#fff}
.tab-active{left:344px;top:421px;width:76px;height:40px}
.ribbon{overflow:hidden}
.ribbon span{position:absolute;background:var(--orange);color:#fff;font-family:"PT Sans",sans-serif;font-size:12px;text-align:center;transform:rotate(45deg)}

/* login */
.login-box{left:533px;top:379px;width:157px;height:154px;background:var(--dark);border-radius:4px}
.login-box .label{position:absolute;left:9px;top:31px;font-size:10px;color:#fff}
.login-box .field{position:absolute;left:25px;width:115px;height:16px;background:#fff}
.login-box .btn{position:absolute;top:98px;height:18px;background:var(--orange);color:#fff;font-weight:700;font-size:10.5px;text-align:center;line-height:18px;border-top:1px solid #f7a15c}
.login-box .opt{position:absolute;left:9px;font-size:10.5px;color:#fff;display:flex;align-items:center;gap:10px}
.login-box .opt i{width:9px;height:9px;border-radius:50%;border:2px solid #fff;background:#222;display:block}
.login-box .opt i.on{background:#7ab6e8}

/* sections */
.section-icon{width:32px;height:32px;border-radius:50%;background:var(--orange);display:flex;align-items:center;justify-content:center}
.section-title{font-family:"PT Sans",sans-serif;font-weight:400;font-size:18px;color:#222}
.body-copy{left:97px;width:410px;font-family:"Lato",sans-serif;font-size:12.4px;line-height:14.5px;color:#444;letter-spacing:.55px;white-space:nowrap}
.video-still{left:96px;top:624px;width:403px;height:161px;background:linear-gradient(100deg,#5a2e14 0%,#8d6a4e 30%,#2e3b55 55%,#1b2337 100%)}
.play{left:226px;top:687px}

/* daily news */
.news-title{left:547px;top:546px;font-family:"PT Sans",sans-serif;font-size:11px;color:#222}
.news-item{left:520px;width:188px;height:60px;border-bottom:1px solid var(--line)}
.news-item .thumb{position:absolute;left:5px;top:1px;width:36px;height:35px;background:#000}
.news-item h4{position:absolute;left:50px;top:0;font-size:7px;font-weight:400;color:var(--orange)}
.news-item .date{position:absolute;left:50px;top:11px;font-size:6px;color:#aaa;font-style:italic}
.news-item p{position:absolute;left:50px;top:23px;width:135px;font-size:6.5px;line-height:9.5px;color:#444}

/* carousel */
.car-arrow{width:11px;height:11px;border-radius:50%;background:#777;overflow:hidden}
.car-thumb{top:888px;height:70px}

/* footer */
.footer-rule{left:77px;top:981px;width:626px;height:2px;background:#f8b487}
.footer-col{top:1009px;width:140px}
.footer-col h3{font-family:"Open Sans",sans-serif;font-weight:400;font-size:10px;color:#fff;margin-bottom:11px}
.footer-col li{list-style:none;font-size:7px;color:#fbc29c;height:17.6px;padding-left:13px;position:relative}
.footer-col li::before{content:"→";position:absolute;left:0;top:-1px;color:#fff;font-size:7px}
.footer-bottom{left:89px;top:1128px;width:600px;height:1px;background:#c9491a}
.copyright{left:89px;top:1141px;font-size:7px;color:#fde0cc;font-style:italic}
</style>
</head>
<body>
<div class="abs orange-floor"></div>

<header>
  <div class="abs brand-box"></div>
  <div class="abs brand-name">vaultmere</div>
  <div class="abs utility"><span>News | Pricelist| Call</span>
    <span class="phone"><svg width="7" height="8" viewBox="0 0 7 8"><circle cx="3.5" cy="2" r="2" fill="#777"/><path d="M0 8c0-3 7-3 7 0z" fill="#777"/></svg><b style="font-weight:600">1300 462 715</b></span>
  </div>
  <div class="abs search">Type your keywords...</div>
  <svg class="abs search-icon" width="15" height="16" viewBox="0 0 15 16"><circle cx="6" cy="6" r="5" fill="none" stroke="#fff" stroke-width="1.6"/><line x1="9.5" y1="10" x2="14" y2="15" stroke="#fff" stroke-width="2"/></svg>
</header>

<nav class="abs main-nav">
  <a style="left:0;width:62px">Home</a><span class="sep" style="left:62px"></span>
  <a style="left:63px;width:59px">Solutions</a><span class="sep" style="left:122px"></span>
  <a style="left:123px;width:74px">Services</a><span class="sep" style="left:197px"></span>
  <a style="left:198px;width:73px">Support</a><span class="sep" style="left:271px"></span>
  <a style="left:272px;width:80px">Partners</a><span class="sep" style="left:352px"></span>
  <a style="left:353px;width:68px">About</a><span class="sep" style="left:421px"></span>
  <a style="left:422px;width:62px">Download</a><span class="sep" style="left:484px"></span>
  <span class="abs social" style="left:574px" aria-label="Social page link"></span>
  <span class="abs social second" style="left:598px" aria-label="Social feed link"></span>
</nav>

<main>
  <div class="abs panel"></div>

  <section>
    <div class="abs hero-photo" role="img" aria-label="Hard drive engulfed in flames with the word fire"></div>
    <div class="abs hero-side">
      <h2>Adipiscing Sem len<br>Ullamcorper.</h2>
      <p>Curabitur blandit tempus porttitor. Donec ullamcorper nulla non metus auctor fringilla. Nullam quis risus eget urna mollis ornare vel eu leo. Cras justo odio, dapibus ut facilisis in, egestas eget quam.</p>
      <span class="more">Read More</span>
    </div>
    <div class="abs hero-dots"><i></i><i></i><i style="margin-left:6px"></i></div>
    <div class="abs hero-caption"><strong>Adipiscing Sem Ullamcorper</strong><span>Curabitur blandit tempus porttitor. Donec ullamcorper nulla non metus auctor fringilla.</span></div>
  </section>

  <div class="abs cta-band">Call to Action <span class="num">1300 462 715</span></div>

  <section>
    <div class="abs news-widget"></div>
    <div class="abs trial-tab"><div class="inner"></div><span>Trial<br>for<br>FREE</span></div>
    <div class="abs email-field"></div>
    <svg class="abs mail-icon" width="21" height="15" viewBox="0 0 21 15"><rect x="1" y="1" width="19" height="13" fill="#fff" stroke="#999"/><path d="M1 1l9.5 8L20 1M1 14l7-6M20 14l-7-6" fill="none" stroke="#888"/></svg>
    <div class="abs tab-active"><svg width="76" height="40" viewBox="0 0 76 40"><path d="M0 0h76v34l-38 6-38-6z" fill="#f07a23"/></svg></div>
    <span class="abs widget-tabs" style="left:161px">Newsletter</span>
    <span class="abs widget-tabs" style="left:263px">Services</span>
    <span class="abs widget-tabs" style="left:349px">Support</span>
    <span class="abs widget-tabs" style="left:432px">Contact</span>
    <div class="abs ribbon" style="left:455px;top:362px;width:75px;height:75px"><span style="left:0;top:24px;width:100px;height:20px;line-height:20px">Sign up</span></div>
  </section>

  <aside>
    <div class="abs login-box">
      <span class="label">Sign in</span>
      <svg class="abs" style="left:10px;top:53px" width="9" height="10" viewBox="0 0 9 10"><circle cx="4.5" cy="2.5" r="2.5" fill="#fff"/><path d="M0 10c0-4 9-4 9 0z" fill="#fff"/></svg>
      <div class="field" style="top:50px"></div>
      <svg class="abs" style="left:10px;top:75px" width="9" height="11" viewBox="0 0 9 11"><path d="M2 5V3a2.5 2.5 0 015 0v2" fill="none" stroke="#fff" stroke-width="1.5"/><rect x="0" y="5" width="9" height="6" fill="#fff"/></svg>
      <div class="field" style="top:73px"></div>
      <div class="btn" style="left:12px;width:65px">Sign up</div>
      <div class="btn" style="left:81px;width:66px">Ok</div>
      <div class="opt" style="top:124px"><i></i>Create new account</div>
      <div class="opt" style="top:136px"><i class="on"></i>Request new password</div>
    </div>
    <div class="abs ribbon" style="left:633px;top:376px;width:60px;height:60px"><span style="left:-4px;top:14px;width:90px;height:18px;line-height:18px">Login</span></div>

    <div class="abs section-icon" style="left:522px;top:544px;width:18px;height:18px"><svg width="8" height="8" viewBox="0 0 8 8"><path d="M0 3h2l3-3v8L2 5H0z" fill="#fff"/></svg></div>
    <div class="abs news-title">Daily News</div>
    <article class="abs news-item" style="top:574px"><div class="thumb"></div><h4>Aenean Lorem Fringilla</h4><span class="date">Posted on 12 Jul 2012</span><p>Lorem ipsum dolor sit amet, consectetur adipiscing elit. e dapibus, tellus ac.</p></article>
    <article class="abs news-item" style="top:637px"><div class="thumb"></div><h4>Condimentum Fusce Venenatis</h4><span class="date">Posted on 12 Jul 2012</span><p>Lorem ipsum dolor sit amet, consectetur adipiscing elit. e dapibus, tellus ac.</p></article>
    <article class="abs news-item" style="top:699px"><div class="thumb"></div><h4>&nbsp;Ipsum Justo Commodo</h4><span class="date">Posted on 12 Jul 2012</span><p>Lorem ipsum dolor sit amet, consectetur adipiscing elit. e dapibus, tellus ac.</p></article>
  </aside>

  <section>
    <div class="abs section-icon" style="left:95px;top:461px"><svg width="11" height="11" viewBox="0 0 10 10"><path d="M5 0l1.5 3.3 3.5.4-2.6 2.4.7 3.5L5 7.8 1.9 9.6l.7-3.5L0 3.7l3.5-.4z" fill="#fff"/></svg></div>
    <h2 class="abs section-title" style="left:138px;top:466px">About us</h2>
    <p class="abs body-copy" style="top:500px">Morbi leo risus, porta ac consectetur ac, vestibulum at<br>estibulum id ligula porta felis euismod semper.Nulla vite<br>libero, a pharetra augue. Donec ullamcorper nulla nonu<br>s auctor fringilla.</p>

    <div class="abs section-icon" style="left:95px;top:572px"><svg width="9" height="11" viewBox="0 0 9 11"><rect x="0" y="0" width="9" height="11" rx="1" fill="#fff"/><rect x="2.5" y="2" width="4" height="7" fill="#f06a1c"/></svg></div>
    <h2 class="abs section-title" style="left:138px;top:577px;font-size:16px">Video Help</h2>
    <div class="abs video-still" role="img" aria-label="Video still of a hard drive beside error messages with the word crash"></div>
    <svg class="abs play" width="44" height="44" viewBox="0 0 44 44"><circle cx="22" cy="22" r="21" fill="rgba(255,255,255,.35)" stroke="rgba(255,255,255,.6)" stroke-width="2"/><path d="M17 12l15 10-15 10z" fill="rgba(255,255,255,.75)"/></svg>
    <p class="abs body-copy" style="top:804px">Morbi leo risus, porta ac consectetur ac, vestibulum at<br>estibulum id ligula porta felis euismod semper.Nulla vite<br>libero, a pharetra augue. Donec ullamcorper nulla nonu<br>s auctor fringilla.</p>
  </section>

  <section>
    <div class="abs car-arrow" style="left:106px;top:918px"><svg width="11" height="11" viewBox="0 0 11 11"><path d="M6.5 3L4 5.5 6.5 8" fill="none" stroke="#fff" stroke-width="1.4"/></svg></div>
    <div class="abs car-thumb" style="left:138px;width:88px;background:linear-gradient(#e88a1a,#b23a0c)" role="img" aria-label="Cartoon computer on fire"></div>
    <div class="abs car-thumb" style="left:243px;width:84px;background:linear-gradient(#e8e8e8,#8a8a8a)" role="img" aria-label="Laptop secured with a padlock"></div>
    <div class="abs car-thumb" style="left:350px;width:88px;background:linear-gradient(#eef0f2,#6b7585)" role="img" aria-label="Office worker at a laptop"></div>
    <div class="abs car-thumb" style="left:455px;width:87px;background:linear-gradient(#5d7a3a,#c96a1e)" role="img" aria-label="Cartoon of a burning computer at a desk"></div>
    <div class="abs car-thumb" style="left:557px;width:86px;background:linear-gradient(#f4f4f4,#c8b39a)" role="img" aria-label="Coffee spilled on a keyboard"></div>
    <div class="abs car-arrow" style="left:664px;top:918px"><svg width="11" height="11" viewBox="0 0 11 11"><path d="M4.5 3L7 5.5 4.5 8" fill="none" stroke="#fff" stroke-width="1.4"/></svg></div>
  </section>
</main>

<footer>
  <div class="abs footer-rule"></div>
  <div class="abs footer-col" style="left:89px"><h3>Our Company</h3><ul><li>About us</li><li>In The Press</li><li>Testimonials</li><li>Site Security</li></ul></div>
  <div class="abs footer-col" style="left:243px"><h3>Our Solutions</h3><ul><li>About us</li><li>In The Press</li><li>Testimonials</li><li>Site Security</li></ul></div>
  <div class="abs footer-col" style="left:397px"><h3>Our Services</h3><ul><li>About us</li><li>In The Press</li><li>Testimonials</li><li>Site Security</li></ul></div>
  <div class="abs footer-col" style="left:550px"><h3>Download</h3><ul><li>About us</li><li>In The Press</li><li>Testimonials</li><li>Site Security</li></ul></div>
  <div class="abs footer-bottom"></div>
  <p class="abs copyright">Copy right 2013 All right reserved &copy; vaultmere</p>
</footer>
</body>
</html>
```